Create a small A5 sized booklet out of a few Word files

The booklet contains instructions for patients who have had surgery. There are about six A4 pages of text which need to be re-formatted and designed into an A5 sized booklet. And a simple front cover for the booklet that says something like "Calloway Centre for Bariatric Surgery. Post operative instructions for bariatric patients"

```html
<!DOCTYPE html>
<html lang="en">
<head>
<meta charset="utf-8">
<title>Calloway Centre for Bariatric Surgery – Post Operative Instructions</title>
<link href="https://fonts.googleapis.com/css2?family=Open+Sans:wght@400;600;700&display=swap" rel="stylesheet">
<style>
:root{
  --teal:#14756d;
  --teal-text:#16857b;
  --teal-soft:#1f8f84;
  --grey-band:#6f7072;
  --grey-title:#66686a;
  --ink:#5a5c5e;
  --rule:#cfd3d3;
  --page:#ffffff;
  --bg:#dcdcdc;
  --photo-a:#1b8fa6;
  --photo-b:#0f5e73;
}
*{box-sizing:border-box;margin:0;padding:0}
html,body{width:1200px;height:833px;overflow:hidden;background:var(--bg);font-family:"Open Sans",Arial,sans-serif;color:var(--ink)}
.spread{position:absolute;left:210px;width:780px;height:372px;display:flex;background:var(--page);box-shadow:0 2px 6px rgba(0,0,0,.15)}
.spread--outer{top:30px}
.spread--inner{top:432px}
.panel{position:relative;width:260px;height:100%;overflow:hidden;border-right:1px solid #e6e6e6;display:flex;flex-direction:column}
.panel:last-child{border-right:none}
.bar{background:var(--teal);color:#fff;font-weight:700;font-size:7px;padding:9px 14px 4px;height:22px;flex:none}
.panel-body{padding:4px 14px 0;flex:1;overflow:hidden}
.h-sub{color:var(--teal-text);font-weight:700;font-size:7.4px;margin:1px 0 3px}
.h-sec{color:var(--teal-text);font-weight:700;font-size:6px;margin:5px 0 2px}
.h-sec--lg{font-size:7.4px}
p,li{font-size:3.9px;line-height:1.35}
.lead{font-weight:600;color:#3e4042;font-size:4px}
ul{list-style:none;margin:2px 0 3px 14px}
li{position:relative;padding-left:7px;margin-bottom:2.6px}
li::before{content:"";position:absolute;left:0;top:1px;width:2.6px;height:2.6px;border-radius:50%;background:var(--teal)}
li.sub{margin-left:10px}
li.sub::before{background:#888}
.foot-band{height:22px;background:var(--grey-band);flex:none}
.photo{flex:none;background:linear-gradient(135deg,var(--photo-a),var(--photo-b))}
.schedule{width:100%;border-collapse:collapse;margin-top:3px}
.schedule th{text-align:left;font-size:4.6px;color:var(--teal-text);font-weight:700;border-top:1px solid var(--teal);border-bottom:1px solid var(--teal);padding:1px 0}
.schedule td{font-size:3.7px;padding:2.6px 1px;vertical-align:top;line-height:1.3}
.schedule td:nth-child(2){text-align:center}
/* cover */
.cover{background:linear-gradient(180deg,#fff 0%,#eef0f0 30%,#d7dadb 45%)}
.brand{display:flex;align-items:center;gap:5px;justify-content:center;margin-top:8px}
.brand-square{width:16px;height:16px;background:var(--teal)}
.brand-name{font-size:6.4px;font-weight:600;color:var(--teal);line-height:1.15}
.cover-title{color:var(--grey-title);font-weight:700;font-size:14.5px;line-height:1.05;text-align:center;margin:9px 0 4px}
.cover-photo{flex:1;margin:0;border-top-left-radius:70px 40px;background:linear-gradient(150deg,#49b6c9,#1d7f9c 45%,#0e5068)}
.cover-band{height:40px;background:var(--grey-band);color:#fff;font-weight:600;font-size:10px;line-height:1.1;text-align:center;padding-top:4px;flex:none}
/* inner */
.cols{display:flex;gap:8px}
.cols>div{flex:1}
.grey-head{background:var(--grey-band);color:#fff;font-weight:600;font-size:6.6px;padding:2px 14px;margin:4px -14px 3px}
.note-row{display:flex;align-items:flex-end;gap:6px;margin-top:auto}
.note{width:95px;background:var(--teal);color:#fff;border-radius:10px 10px 10px 10px;padding:5px 6px 6px;text-align:center}
.note h4{font-size:5.4px;line-height:1.15;margin-bottom:2px}
.note p{font-size:3.5px}
.note-photo{flex:1;height:85px;background:linear-gradient(135deg,#c7dfe6,#5c98ab)}
.p4{display:flex;flex-direction:column;height:100%}
</style>
</head>
<body>

<!-- Outer side: pages 5, 6 and cover -->
<section class="spread spread--outer">
  <article class="panel">
    <div class="bar">Discharge Information - Complications,</div>
    <div class="panel-body">
      <h2 class="h-sub">Red Flags and Contacts</h2>
      <p class="lead">Serious complications are uncommon after straight forward bariatric procedures however from time to time they will occur. Early diagnosis and treatment always leads to best outcomes.</p>
      <h3 class="h-sec">Things to watch out for…</h3>
      <ul>
        <li>Fevers or sweats that continue unabated</li>
        <li>Measured temperature greater than 38.0 degrees – unabated</li>
        <li>Increasing abdominal pain, unabated</li>
        <li>Difficulties breathing</li>
        <li>Continuous vomiting</li>
        <li>Vomiting blood</li>
      </ul>
      <p>The above issues should trigger you or your carer to contact us.</p>
      <h3 class="h-sec">Important Contact Information</h3>
      <ul>
        <li>If you are feeling extremely sick or vomiting blood call an ambulance.</li>
        <li>If you have less urgent concerns about your condition call the rooms to discuss on 9000 1100</li>
        <li>After hours if you have urgent concerns text (preferred) or call Mr Harlow on 0400 000 111 or Ms Varga on 0400 000 222</li>
      </ul>
      <p>If you decide to present to a hospital emergency department the following are best options:</p>
      <ul>
        <li><b>Eastfield Public Hospital.</b></li>
        <li class="sub">No cost involved. Occasionally significant waiting times to be seen initially</li>
        <li><b>Northgate Private Hospital</b></li>
        <li class="sub">If you have private insurance this may allow you to be seen quicker</li>
        <li><b>Other local hospital or regional hospital.</b></li>
        <li class="sub">Relevant expertise may not be available hence it is always worth contacting our rooms to let us know you are attending.</li>
      </ul>
      <p>Note that it is best to discuss with Mr Harlow or Ms Varga prior to presenting to emergency departments as he can advise the best option given your particular circumstances.</p>
      <h3 class="h-sec">Discharge Information - Introduction &amp; Appointment Schedule</h3>
      <p>Congratulations on the commencement of your weight loss journey! Enclosed are some small items and information that will help you manage the first stages of your recovery. From all of us at CCBS we wish you the very best of good fortune and a smooth recovery ongoing!</p>
      <h3 class="h-sec">Standard Appointment Schedule first 12 months.</h3>
      <ul>
        <li>Variations on this will depend on your individual progress and needs.</li>
        <li>Please note – unless you have pre-arranged your first post op surgeon's appointment you will need to call or email the rooms after discharge to organise this appointment.</li>
      </ul>
    </div>
    <div class="foot-band"></div>
  </article>

  <article class="panel">
    <div class="bar">Discharge Information</div>
    <div class="panel-body">
      <h2 class="h-sub">Introduction &amp; Appointment Schedule</h2>
      <p>Congratulations on the commencement of your weight loss journey! Enclosed are some small items and information that will help you manage the first stages of your recovery. From all of us at CCBS we wish you the very best of good fortune and a smooth recovery ongoing!</p>
      <h3 class="h-sec">Standard Appointment Schedule first 12 months.</h3>
      <ul>
        <li>Variations on this will depend on your individual progress and needs.</li>
        <li>Please note – unless you have pre-arranged your first post op surgeon's appointment you will need to call or email the rooms after discharge to organise this appointment.</li>
      </ul>
      <h3 class="h-sec">Schedule</h3>
      <table class="schedule">
        <thead><tr><th>Event</th><th>Time Post op</th><th>Comment</th></tr></thead>
        <tbody>
          <tr><td>Phone call from dietician</td><td>1-2 weeks</td><td></td></tr>
          <tr><td>Post op appointment with surgeon</td><td>2 weeks</td><td>Timing may vary according to availability of local consulting</td></tr>
          <tr><td>Second appointment with dietician</td><td>3 months</td><td>May vary depending on your dietician</td></tr>
          <tr><td>Second appointment with surgeon</td><td>3 months</td><td></td></tr>
          <tr><td>First nutritional screen (blood test) sent out (SIPS patients only)</td><td>3 months</td><td>SIPS patients only. Aim to complete blood test prior to surgeon's appointment</td></tr>
          <tr><td>First nutritional screen sent out (all other patients)</td><td>6 months</td><td>Except SIPS patients – this will be the 2nd screen</td></tr>
          <tr><td>Third appointment with dietician</td><td>6 months</td><td>Dependent on discussions with your dietician</td></tr>
          <tr><td>Second nutritional screen sent out</td><td>12 months</td><td>Ideally have the screen done prior to your 12 month surgical review</td></tr>
          <tr><td>Third appointment with surgeon</td><td>12 months</td><td></td></tr>
        </tbody>
      </table>
    </div>
    <div class="photo" style="height:100px" role="img" aria-label="Photograph of a surgical team operating in theatre"></div>
  </article>

  <article class="panel cover">
    <div class="brand">
      <span class="brand-square"></span>
      <span class="brand-name">Calloway Centre<br>for Bariatric Surgery</span>
    </div>
    <h1 class="cover-title">Calloway Centre for<br>Bariatric Surgery</h1>
    <div class="cover-photo" role="img" aria-label="Photograph of a surgeon in scrubs and cap in an operating theatre"></div>
    <div class="cover-band">Post Operative Instructions<br>for Bariatric Patients</div>
  </article>
</section>

<!-- Inner side: pages 2, 3 and 4 -->
<section class="spread spread--inner">
  <article class="panel">
    <div class="bar">General Information and Frequently Asked Questions</div>
    <div class="panel-body">
      <h2 class="h-sub">General Advice</h2>
      <p class="lead">You should be mobile and on your feet from the day of discharge. Apart from general recovery this will help prevent clots forming in your legs (deep venous thrombosis)</p>
      <div class="cols">
        <div>
          <h3 class="h-sec">Work</h3>
          <p>Most people will be fine to return to work after two weeks. Some with office jobs or home based work may prefer to go back after one week or even earlier. Physically demanding jobs where heavy lifting or strenuous activity is required should only be recommenced after four weeks unless light duties can be allocated.</p>
          <h3 class="h-sec">Walking</h3>
          <p>You can go walking outside the house as soon as you feel comfortable. Aim to increase the amount of walking progressively over the weeks after your surgery.</p>
          <h3 class="h-sec">Swimming</h3>
          <p>Swimming is fine one week post surgery as long as you have well attached, waterproof dressings. After the dressings have been removed, swimming is ok as long as all the wounds are nicely sealed and no longer gaping.</p>
          <h3 class="h-sec">Gym</h3>
          <p>Cardio exercises like running, power walking, step machine etc are fine from two weeks post surgery. Lifting weights should not occur until at least four weeks.</p>
          <h3 class="h-sec">Driving</h3>
          <p>You can drive a car 5 days after surgery as long as your pain levels are under control and you are no longer requiring strong or sedative pain killers.</p>
          <h3 class="h-sec">Lifting</h3>
          <p>Heavy lifting should be avoided until 4 weeks post surgery. Avoid lifting 10kg or more.</p>
        </div>
        <div>
          <p>more during this time if practical. Lifting small children is sometimes unavoidable however find other alternatives where possible. Strenuous pushing and pulling activities should be treated similarly.</p>
          <h3 class="h-sec">Anti-inflammatories</h3>
          <p>This class of drugs (NSAIDs) include common pain relief tablets sold at pharmacies. These medications can irritate the stomach and bowel and in some cases cause ulceration. Ideally they are to be avoided in the first 6 weeks after surgery to encourage healing of the tissues. If required regularly and ongoing in most cases it is best to take a low dose acid reducing tablet as well to protect the stomach and bowel lining. This is particularly important in gastric bypass surgery.</p>
          <h3 class="h-sec">Alcohol</h3>
          <p>Avoiding alcohol for six weeks after surgery is sensible whilst the surgery is healing. Going forward be mindful that alcohol will affect you more quickly and its effects may be stronger after having bariatric surgery. If you are driving be aware that your blood alcohol level may rise faster with less standard drinks than with a normal stomach.</p>
          <h3 class="h-sec">Sex</h3>
          <p>A common sense approach should be taken with respect to sexual activity. After four weeks there are no specific restrictions on any activities. With care sexual activity could potentially resume earlier as long as you feel comfortable and pain free.</p>
        </div>
      </div>
      <div class="grey-head">Wounds</div>
      <h3 class="h-sec">Dressings</h3>
      <p>The dressings should be waterproof and allow you to shower. If the dressings are tatty, dirty or blood-soaked in the first ten days you can change one or more dressings with the replacements provided. Dressings can otherwise be removed by anyone including yourself after 10 days or you can wait until your post-operative appointment.</p>
      <h3 class="h-sec">Lumps, Threads</h3>
      <p>Lumpiness under the wound is typical and will resolve over several weeks. If you see suture thread sticking up from a corner of the wound it may need to be removed. Your doctor can</p>
    </div>
  </article>

  <article class="panel">
    <div class="bar" style="background:var(--teal)">&nbsp;</div>
    <div class="panel-body">
      <p>do this or if you are feeling brave, pick up the thread with tweezers, pull as much out as you can then cut it off at skin level.</p>
      <h3 class="h-sec">Discomfort, pain</h3>
      <p>It is normal to experience some discomfort, pain or pulling related to one or more wounds either at skin level or deeper. Discomfort should improve with time.</p>
      <h3 class="h-sec">Redness, smelliness, pus</h3>
      <p>These are signs of possible wound infection. You should organise to be seen by your GP or surgeon and a short antibiotic course may be necessary.</p>
      <h3 class="h-sec">Allergy, intolerance to dressings</h3>
      <p>Many patients have minor allergies or intolerances to dressings. If the skin becomes excessively itchy or red underneath the whole extent of the dressing it is best simply to remove the dressing and leave the wound uncovered.</p>
      <div class="grey-head">Symptoms</div>
      <div class="cols">
        <div>
          <h3 class="h-sec">Pain</h3>
          <p>If you have been discharged from hospital, your pain levels should be well manageable with oral tablets. For most patients simple pain relief is the basis of pain relief and can be taken regularly every 6 hours. If necessary stronger pain relievers can be taken additionally and are typically chosen by your anaesthetist. If your pain and discomfort is manageable it is preferable to reduce or avoid these stronger tablets as they can contribute to nausea, constipation and general immobility.</p>
          <h3 class="h-sec">Nausea</h3>
          <p>If you are suffering nausea transiently or ongoing, be reassured that this will settle with time. You should have been prescribed anti-nausea medications which you should take as recommended for as long as you need to. Keep track of your fluid intake over the day and how you are feeling generally. If you are tolerating very little fluid (less than 500ml in 24 hours) and are feeling very flat then contact your surgeon.</p>
          <h3 class="h-sec">Reflux</h3>
          <p>Reflux symptoms may be in the form of "heartburn" (a rising burning sensation behind the middle of your chest) or acid or bile coming up into your mouth or the back of your throat. Reflux can sometimes be caused or exacerbated by bariatric procedures. At night it may help to sleep propped up on two or more pillows. Antacid liquids can be used.</p>
        </div>
        <div>
          <p>useful in mild cases. For ongoing significant symptoms a more powerful medication such as an acid reducing tablet can be very helpful. Low dose tablets can be obtained from your chemist without prescription. For higher doses or ongoing requirements seek prescription from your GP or specialist. For more severe intractable cases of reflux where medication is not sufficient further investigation may be warranted and corrective surgery may be possible.</p>
          <h3 class="h-sec">Gas</h3>
          <p>It is a common experience after most bariatric procedures that burping or gas related symptoms can arise. This may be best explained by the fact that the large reservoir of the stomach is no longer able to store gas for periods of time before expelling it. Hence the gas sometimes tends to move wherever it likes! For some people excessive air swallowing during eating, drinking or speaking can exacerbate the problem. Over the counter anti-gas drops can help.</p>
          <h3 class="h-sec">Constipation</h3>
          <p>Reduced intake, dehydration and taking strong pain killers can predispose patients to constipation in the early weeks after surgery. Keeping up with fluid intake and ensuring some fruits and vegetables are part of your diet is the first step. A fibre supplement taken at least twice a day can help, as can a gentle stool softener from your chemist.</p>
        </div>
      </div>
    </div>
  </article>

  <article class="panel">
    <div class="bar">Discharge Information - Basics of the post operative diet</div>
    <div class="panel-body p4">
      <p class="lead" style="color:var(--teal-text)">Dietary phases should be comprehensively covered by your pre and post surgery dietician consultations.</p>
      <p style="margin-top:4px">The following represents only a brief overview to focus your attention on the key points.</p>
      <p style="margin-top:4px">For further details and discussion please contact your dietician for advice or access your written resources.</p>
      <p style="margin-top:4px">I would encourage you not to over-think your food decisions and behaviours too much. Worrying too much about every gram of protein or every drink will only lead to severe anxiety setting in!</p>
      <h3 class="h-sec">These basic rules apply to most patients after bariatric procedures:</h3>
      <ul>
        <li>Two weeks liquid diet (thin liquids) – followed by…</li>
        <li>Two weeks pureed/mashed type foods – followed by…</li>
        <li>Slow introduction of normal solid foods starting with easier textures</li>
      </ul>
      <h3 class="h-sec">Key points</h3>
      <ul>
        <li>Liquids, purees, solids should be nourishing, i.e. not just water or cordial or juice etc.</li>
        <li>Go slowly, stop if you feel full or about to vomit</li>
        <li>You will need to work hard to hydrate yourself properly in the early stages – keep sipping away throughout the day</li>
        <li>Avoid gulps of liquids with solid meals. Separate drinking from eating by about 30 minutes before and after. Catch up on hydration in between solid meals.</li>
        <li>Sitting up makes it easier to get liquid and food down</li>
        <li>For solid foods, half a cup is usually sufficient in the first few months</li>
        <li>Don't keep picking away at your meal for more than 10 minutes – this should be as much time as necessary to complete a meal.</li>
        <li>Ensure you have a high component of protein in your diet</li>
        <li>Start your vitamins usually within two weeks of surgery, as discussed with your dietician</li>
        <li>If you are not tolerating your vitamins, make contact with your dietician to discuss alternatives</li>
      </ul>
      <div class="note-row">
        <aside class="note">
          <h4>A note about weight changes in the early stages:</h4>
          <p>Your weight will vary, sometimes substantially, from day to day particularly early on after your bariatric procedure. Much of this is due to fluid shifts and particularly dehydration in the first couple of weeks. If you choose to weigh yourself daily be prepared for some fairly dramatic shifts which can be disconcerting. Look for changes over weeks rather than days.</p>
        </aside>
        <div class="note-photo" role="img" aria-label="Photograph of a surgeon wearing a cap and mask"></div>
      </div>
    </div>
  </article>
</section>

</body>
</html>
```